Business cards need a revamp and change of address. I have included files of current card which has been used for 5 years. Also a photo of my new store fitout which uses a lot of colour and features inspired by cusco Peru. I would like to see design options with and without the butterfly although I do use the butterfly on my current street signage.
Updates

Reason: would like to see more designers submit

Target Market(s)

women 35 - 65

Industry/Entity Type

Business

Contact Information for Business Card

Larkvale Andean Silver Jewellery & Giftware

Requirements
Must have
• logo frontside
• backside the following text:
• Larkvale Jewellery is hand made using the highest quality 950 Peruvian Silver which is purer than 925 Sterling Silver. Larkvale's range of unique, handcrafted products are directly sourced from fair trade producer co-operatives, individual artisans and artisan groups from Peru, South America.
• Phone 02 43168272
• 7/118 Pelham Road Larkhill VIC 3081
• Email : sales@larkvale.com.au
Nice to have
• Like us on face book

```html
<!DOCTYPE html>
<html lang="en">
<head>
<meta charset="utf-8">
<title>Larkvale Jewellery – Business Card Options</title>
<link href="https://fonts.googleapis.com/css2?family=Tinos:wght@400;700&display=swap" rel="stylesheet">
<style>
  :root {
    --page: #ffffff;
    --card-blue: #0274a4;
    --butterfly-blue: #0ba2c6;
    --ink: #ffffff;
  }
  * { margin: 0; padding: 0; box-sizing: border-box; }
  html, body {
    width: 1200px; height: 1199px; overflow: hidden;
    background: var(--page);
  }
  .sheet { position: relative; width: 1200px; height: 1199px; }
  .card {
    position: absolute; width: 586px; height: 586px; border-radius: 50%;
    background: var(--card-blue); overflow: hidden;
    font-family: "Tinos", "Times New Roman", serif; font-weight: 700; color: var(--ink);
  }
  .card--front-butterfly { left: 0; top: 0; }
  .card--back-butterfly  { left: 614px; top: 0; }
  .card--front-plain     { left: 0; top: 613px; }
  .card--back-plain      { left: 614px; top: 613px; }

  .butterfly {
    position: absolute; left: 60px; top: 138px; width: 478px; height: 348px;
    background: radial-gradient(ellipse at center, var(--butterfly-blue) 0%, rgba(11,162,198,0.75) 70%, rgba(11,162,198,0) 100%);
    border-radius: 45% 45% 40% 40%;
  }

  .wordmark {
    position: absolute; left: 88px; top: 182px;
    font-size: 100px; line-height: 1; letter-spacing: -1px; white-space: nowrap;
  }

  .web {
    position: absolute; left: 0; top: 447px; width: 586px; text-align: center;
    font-size: 16px; line-height: 20px;
  }

  .about {
    position: absolute; left: 126px; width: 345px;
    font-size: 18.5px; line-height: 25.5px;
    text-align: justify; text-align-last: center;
  }
  .card--back-butterfly .about { top: 191px; }
  .card--back-plain .about { top: 167px; }

  .rule {
    position: absolute; left: 126px; top: 408px; width: 342px; height: 5px;
    background: var(--ink);
  }

  .contact {
    position: absolute; left: 0; width: 596px; text-align: center;
    font-size: 12px; line-height: 17.5px;
  }
  .card--back-butterfly .contact { top: 461px; }
  .card--back-plain .contact { top: 419px; }
</style>
</head>
<body>
<main class="sheet">

  <section class="card card--front-butterfly">
    <div class="butterfly" role="img" aria-label="Large faint butterfly illustration in pale turquoise behind the name"></div>
    <div class="wordmark">larkvale</div>
    <div class="web">www.larkvale.com.au</div>
  </section>

  <section class="card card--back-butterfly">
    <div class="butterfly" role="img" aria-label="Large faint butterfly illustration in pale turquoise behind the text"></div>
    <p class="about">Larkvale Jewellery is hand made using the highest quality 950 Peruvian Silver which is purer than 925 Sterling Silver. Larkvale's range of unique, handcrafted products are directly sourced from fair trade producer co-operatives, individual artisans and artisan groups from Peru, South America.</p>
    <div class="contact">
      Phone 02 43168272<br>
      7/118 Pelham Road Larkhill VIC 3081<br>
      Email : sales@larkvale.com.au
    </div>
  </section>

  <section class="card card--front-plain">
    <div class="wordmark">larkvale</div>
    <div class="web">www.larkvale.com.au</div>
  </section>

  <section class="card card--back-plain">
    <p class="about">Larkvale Jewellery is hand made using the highest quality 950 Peruvian Silver which is purer than 925 Sterling Silver. Larkvale's range of unique, handcrafted products are directly sourced from fair trade producer co-operatives, individual artisans and artisan groups from Peru, South America.</p>
    <div class="rule"></div>
    <div class="contact">
      Phone 02 43168272<br>
      7/118 Pelham Road Larkhill VIC 3081<br>
      Email : sales@larkvale.com.au
    </div>
  </section>

</main>
</body>
</html>
```